"Beyond Marrow Cay" Fictional Book Cover

BEYOND MARROW CAY
By: Dale Pruitt

Here's the intro .

"It had been nearly forty years since Ted Larraby last went to the island from where he was raised. Three months earlier he never would have thought about ever coming back. But life is weird. Things happen quickly and plans change, especially when your very life is at stake. The reason he was going back wasn’t to see old friends...no, no, no. They’re all dead. Of all the kids he grew up with on the island who moved off, he’s the only one still alive. Why?"

Pretty much all just a Lumeno book, by the way.

Target Market(s)

fiction readers

Requirements
Must have
• Somewhat of a dark, mysterious cover is what I'd like to see. Use your imagination. I've never written a fiction book before so I'm very open to ideas

Needs to have my name, DALE PRUITT at the bottom. like my other books, all of which are non-fiction
Nice to have
• Mysterious is what I'm looking for. NOT A HORROR story though. More a guy who left the island years ago, but is being called back to escape the rat race of modern, consumerist culture.

Please remember this NEEDS to jump out as a thumbnail on Bookvale as people are browsing. Mainly the WORDS need to stick out. Lighter words on a say a blue background.

If you want to try to use the attached pic, or something like this, to reflect an island in the cover, that'd be good.

I've also uploaded a couple images I purchased from Pixelcrate, hopefully you can make something work with these.

```html
<!DOCTYPE html>
<html lang="en">
<head>
<meta charset="utf-8">
<title>Beyond Marrow Cay — Dale Pruitt</title>
<link rel="stylesheet" href="https://fonts.googleapis.com/css2?family=Bodoni+Moda:opsz,wght@6..96,500;6..96,700;6..96,800&display=swap">
<style>
  :root {
    --page-bg: #9a9a9a;
    --sky-top: #3d3468;
    --sky-mid: #5a4377;
    --glow: #b98a78;
    --glow-soft: #8f6a80;
    --shore: #3a3250;
    --water: #2f2a5c;
    --water-deep: #221c4a;
    --ink-light: #ffffff;
    --ink-shadow: rgba(30, 14, 20, 0.85);
  }
  * { margin: 0; padding: 0; box-sizing: border-box; }
  html, body {
    width: 720px;
    height: 1200px;
    overflow: hidden;
    background: var(--page-bg);
  }
  .book-cover {
    position: absolute;
    left: 40px;
    top: 127px;
    width: 640px;
    height: 946px;
    overflow: hidden;
    box-shadow: 8px 10px 14px rgba(0, 0, 0, 0.35);
  }
  .cover-photo {
    position: absolute;
    inset: 0;
    background: linear-gradient(
      to bottom,
      var(--sky-top) 0%,
      var(--sky-mid) 26%,
      var(--glow-soft) 34%,
      var(--glow) 43%,
      var(--glow-soft) 48%,
      var(--shore) 54%,
      var(--water) 64%,
      var(--water-deep) 100%
    );
  }
  .title {
    position: absolute;
    left: 0;
    right: 0;
    top: 92px;
    text-align: center;
    color: var(--ink-light);
    font-family: "Bodoni Moda", "Didot", serif;
    text-shadow: 3px 3px 3px var(--ink-shadow);
  }
  .title-line-1 {
    display: block;
    font-size: 186px;
    font-weight: 500;
    line-height: 1;
    letter-spacing: -2px;
    transform: scaleX(0.6);
    transform-origin: center;
    margin-left: 40px;
  }
  .title-line-2 {
    display: block;
    margin-top: -6px;
    font-size: 64px;
    font-weight: 800;
    line-height: 1;
    letter-spacing: 1px;
    margin-left: 40px;
  }
  .author {
    position: absolute;
    left: 0;
    right: 0;
    top: 830px;
    text-align: center;
    color: var(--ink-light);
    font-family: "Bodoni Moda", "Didot", serif;
    font-size: 52px;
    font-weight: 700;
    letter-spacing: 1px;
    line-height: 1;
  }
</style>
</head>
<body>
  <main class="book-cover">
    <div class="cover-photo" role="img" aria-label="Photograph of an island ferry dock and shoreline under a purple and peach dusk sky, with dark water in the foreground"></div>
    <h1 class="title">
      <span class="title-line-1">BEYOND</span>
      <span class="title-line-2">MARROW CAY</span>
    </h1>
    <p class="author">DALE PRUITT</p>
  </main>
</body>
</html>
```